BrushGuard Tolland- Making Helena A Wildfire Adapted Community

Design a two complimentary graphics with text that can be used for a banner and "mini-billboard" to promote the project and encourage citizens to go to the webpage to learn more. Using the attached document as examples of what we want the two banners to say.
The goal of BrushGuard Tolland is to plan and prepare so if an urban wildfire occurs, catastrophic loss can be avoided. BrushGuard Tolland focuses on reducing the risk of and catastrophic losses to resources and private property on private land in Helena, MT. Property owners are encouraged to be proactive to address hazardous fuel conditions on their property, reduce structure ignition potential within their home ignition zone and employ wildfire resilient principles to sustain a fire adapted home, property and community. Ember showers from a wildfire next to the city is the biggest concern.

Target Market(s)

Residents in the project area of Helena. Signs and banners will be displayed on public lands and private yeards

Font styles to use
Sans Serif

Requirements
Must have
• Graphics, use of the MeadowlineBlaze Watch Planning Circle logo. Must incorporate the text that is part of the attachment.
Nice to have
• Get people's attention. A simple graphic that get's people's attention.
Should not have
• small details.

```html
<!DOCTYPE html>
<html lang="en">
<head>
<meta charset="utf-8">
<title>BrushGuard Tolland – Ignition Resistant Space Banner</title>
<link rel="stylesheet" href="https://fonts.googleapis.com/css2?family=Montserrat:wght@600;700;800&display=swap">
<style>
  :root {
    --bg: #050505;
    --white: #ffffff;
    --amber: #f9a11b;
    --orange: #f7901e;
    --flame-red: #ff4b1f;
    --yellow: #ffd400;
    --gold: #ffb400;
    --green: #2f7f1e;
    --green-light: #6cbf2a;
    --logo-tint: #e9ec93;
  }
  * { margin: 0; padding: 0; box-sizing: border-box; }
  html, body {
    width: 1200px;
    height: 402px;
    overflow: hidden;
    background: var(--bg);
  }
  .banner {
    position: relative;
    width: 1200px;
    height: 402px;
    overflow: hidden;
    background: var(--bg);
    font-family: "Montserrat", Arial, sans-serif;
  }
  .fire-photo {
    position: absolute;
    right: 0;
    top: 0;
    width: 520px;
    height: 402px;
    background:
      radial-gradient(ellipse 60% 55% at 85% 70%, rgba(255,120,20,0.95) 0%, rgba(220,60,10,0.75) 35%, rgba(120,20,5,0.35) 65%, rgba(5,5,5,0) 100%),
      radial-gradient(ellipse 40% 40% at 95% 20%, rgba(200,50,10,0.55) 0%, rgba(5,5,5,0) 100%);
  }
  .headline {
    position: absolute;
    left: 60px;
    top: 64px;
    color: var(--white);
    font-weight: 700;
    font-size: 39px;
    line-height: 47px;
    letter-spacing: -0.2px;
  }
  .headline .accent { font-weight: 800; }
  .headline .accent--amber { color: var(--amber); }
  .headline .accent--orange { color: var(--orange); }
  .headline .accent--red { color: var(--flame-red); }
  .house-fire-graphic {
    position: absolute;
    left: 497px;
    top: 44px;
    width: 214px;
    height: 292px;
    border-radius: 46% 46% 10% 10%;
    background:
      radial-gradient(ellipse 55% 40% at 50% 72%, rgba(120,210,40,0.95) 0%, rgba(40,140,40,0.85) 45%, rgba(255,75,31,0) 80%),
      linear-gradient(180deg, #ff5a24 0%, #ff4519 60%, #e8380f 100%);
  }
  .call-to-action {
    position: absolute;
    left: 838px;
    top: 56px;
    width: 260px;
    text-align: center;
    color: var(--yellow);
    font-weight: 700;
    font-size: 18px;
    line-height: 22px;
    letter-spacing: 0.3px;
  }
  .call-to-action .emphasis { color: var(--gold); }
  .group-name {
    position: absolute;
    left: 880px;
    top: 220px;
    width: 210px;
    display: flex;
    align-items: center;
    gap: 10px;
  }
  .group-name__mark {
    flex: none;
    width: 26px;
    height: 26px;
    border-radius: 50%;
    background: var(--logo-tint);
  }
  .group-name__text {
    color: var(--logo-tint);
    font-weight: 700;
    font-size: 16px;
    line-height: 20px;
  }
  .info-bar {
    position: absolute;
    left: 448px;
    top: 362px;
    width: 752px;
    height: 21px;
    background: linear-gradient(90deg, rgba(47,127,30,0) 0%, var(--green) 22%, var(--green) 100%);
    display: flex;
    align-items: center;
    justify-content: flex-end;
    padding-right: 22px;
    font-size: 13px;
    font-weight: 700;
    color: var(--white);
    gap: 8px;
  }
  .info-bar__url { color: var(--yellow); }
</style>
</head>
<body>
  <main class="banner">
    <div class="fire-photo" role="img" aria-label="Photograph of close-up wildfire flames glowing orange and red"></div>

    <h1 class="headline">
      The best way to<br>
      KEEP <span class="accent accent--amber">YOUR HOME</span><br>
      from <span class="accent accent--orange">BURNING</span><br>
      is to keep it from<br>
      <span class="accent accent--red">CATCHING FIRE</span><br>
      in the first place.
    </h1>

    <div class="house-fire-graphic" role="img" aria-label="Illustration of a green house and tree surrounded by orange-red flames"></div>

    <p class="call-to-action">
      PROTECT <span class="emphasis">YOUR HOME</span><br>
      <span class="emphasis">FROM WILDFIRE</span><br>
      CREATE IGNITION<br>
      RESISTANT SPACE
    </p>

    <div class="group-name">
      <span class="group-name__mark"></span>
      <span class="group-name__text">MeadowlineBlaze Watch Planning Circle</span>
    </div>

    <footer class="info-bar">
      <span class="info-bar__lead">Learn more at BRUSHGUARD TOLLAND</span>
      <span class="info-bar__url">WWW.MBWPC.ORG</span>
    </footer>
  </main>
</body>
</html>
```